Retractable Banner Design Featuring Key Product for Beauty Trade Show

We're a beauty/nail supply company that specializes in products used in professional nail salons. The key product for this design is Disposable Latex Gloves.
We will be exhibiting in a trade show this summer and are looking for a free-standing Retractable Banner Design that will be displayed at the front of our booth. The goal of the banner will be to display key products that are high in demand with our customers. The banner will be used to attract attention and highlight key selling points of these popular products. We would like the banner to be focused on the product title, image and key points, with a beauty/model/pattern background to create a professional appearance.
Nail Salons
Nail & Beauty Industry

```html
<!DOCTYPE html>
<html lang="en">
<head>
<meta charset="utf-8">
<title>Latex Gloves – Retractable Banner</title>
<link rel="stylesheet" href="https://fonts.googleapis.com/css2?family=Montserrat:wght@500;700;900&display=swap">
<style>
  :root {
    --orange: #f26a1b;
    --orange-deep: #e2550c;
    --orange-light: #f89a4a;
    --ink: #1e1e1e;
    --white: #ffffff;
    --grey-soft: #eeeeee;
    --grey-mid: #e2e2e2;
  }
  * { margin: 0; padding: 0; box-sizing: border-box; }
  html, body { width: 800px; height: 1200px; overflow: hidden; background: var(--white); }
  body { font-family: "Montserrat", sans-serif; color: var(--ink); }

  .banner { position: relative; width: 800px; height: 1200px; overflow: hidden; }
  .banner-background { position: absolute; inset: 0; }

  .product-title {
    position: absolute; left: 80px; top: 70px;
    font-weight: 900; font-size: 118px; line-height: 0.95;
    color: var(--orange); letter-spacing: -1px; text-transform: uppercase;
  }
  .title-tag {
    position: absolute; left: 84px; top: 318px;
    width: 400px; height: 36px; background: var(--orange);
    color: var(--white); font-weight: 700; font-size: 17px;
    letter-spacing: 2px; display: flex; align-items: center; justify-content: center;
  }
  .pack-points { position: absolute; left: 84px; top: 384px; list-style: none; }
  .pack-points li {
    position: relative; padding-left: 26px; margin-bottom: 10px;
    font-size: 26px; font-weight: 500; line-height: 1.15;
  }
  .pack-points li strong { font-weight: 900; }
  .pack-points li::before {
    content: ""; position: absolute; left: 0; top: 10px;
    width: 12px; height: 12px; border-radius: 50%; background: var(--orange);
  }

  .gloves-photo {
    position: absolute; left: 40px; top: 520px; width: 400px; height: 380px;
    background: radial-gradient(ellipse at 50% 45%, #fbf8f2 0%, #efe8dc 55%, rgba(239,232,220,0) 80%);
  }

  .feature-points { position: absolute; left: 478px; top: 580px; width: 290px; list-style: none; }
  .feature-points li {
    position: relative; padding-left: 24px; margin-bottom: 26px;
    color: var(--white); font-size: 21px; font-weight: 700; line-height: 1.25;
  }
  .feature-points li::before {
    content: ""; position: absolute; left: 0; top: 8px;
    width: 11px; height: 11px; border-radius: 50%; background: var(--white);
  }

  .product-box {
    position: absolute; left: 390px; top: 950px; width: 370px; height: 190px;
    background: linear-gradient(160deg, #ffffff 0%, #fbe2cf 45%, var(--orange-light) 70%, var(--orange-deep) 100%);
    box-shadow: 0 10px 24px rgba(0,0,0,0.25);
  }

  .brand {
    position: absolute; left: 84px; top: 1110px;
    display: flex; align-items: center; gap: 12px;
    color: var(--white); font-weight: 700; font-size: 28px;
  }
  .brand-dot { width: 22px; height: 22px; border-radius: 50%; background: var(--white); }
</style>
</head>
<body>
<main class="banner">
  <svg class="banner-background" width="800" height="1200" viewBox="0 0 800 1200" aria-hidden="true">
    <rect width="800" height="1200" fill="var(--white)"/>
    <polygon points="0,0 330,0 0,300" fill="var(--grey-soft)"/>
    <polygon points="420,0 800,0 800,200 560,360" fill="var(--grey-soft)"/>
    <polygon points="560,0 800,0 800,120" fill="var(--grey-mid)"/>
    <path d="M800 230 C640 300 520 380 440 520 C390 610 300 870 0 950 L0 1200 L800 1200 Z" fill="var(--orange)"/>
    <path d="M800 330 C660 390 560 470 510 560 C470 640 420 900 150 1000 L0 1050 L0 1200 L800 1200 Z" fill="var(--orange-deep)" opacity="0.35"/>
    <path d="M800 230 C640 300 520 380 440 520" fill="none" stroke="var(--white)" stroke-width="10"/>
  </svg>

  <h1 class="product-title">Latex<br>Gloves</h1>
  <div class="title-tag">POWDER-FREE EXAM GLOVES</div>

  <ul class="pack-points">
    <li><strong>1,000 Pcs</strong>/Case</li>
    <li><strong>84 Cases</strong> Per<br>Pallet</li>
  </ul>

  <div class="gloves-photo" role="img" aria-label="Hands pulling on white disposable latex gloves"></div>

  <ul class="feature-points">
    <li>100% Powder-Free – No Additives or Fillers</li>
    <li>Standard Textured Finish for Superior Grip</li>
    <li>8.5g Latex – Super Strong Thick</li>
    <li>Designed For Professional Salons</li>
  </ul>

  <div class="product-box" role="img" aria-label="Boxes of disposable latex gloves"></div>

  <div class="brand"><span class="brand-dot"></span>Lumora Supply</div>
</main>
</body>
</html>
```